Flyer for IT Support Company

We need a 1 sided A5 flyer to promote our services and support packages to local businesses, I have attached the sort of content and layout we are looking for but happy for you to be creative with backgrounds and colors. It needs to look modern and professional but catch the eye ;-)
The strap-line on the logo needs to be changed to to 'Your Local IT Company'

It Company

```html
<!DOCTYPE html>
<html lang="en">
<head>
<meta charset="utf-8">
<title>Corvex – Affordable IT Support Packages</title>
<link href="https://fonts.googleapis.com/css2?family=Arimo:wght@400;700&display=swap" rel="stylesheet">
<style>
:root{
  --page:#eeeeec;
  --lime:#a9c93a;
  --lime-bright:#c4df3c;
  --lime-pale:#d9ec6a;
  --olive:#7d8f2a;
  --pink:#d2168a;
  --pink-deep:#b9157c;
  --pink-hot:#e8147f;
  --ink:#222;
  --white:#fff;
  --rule:#555;
}
*{box-sizing:border-box;margin:0;padding:0}
html,body{width:1200px;height:1000px;overflow:hidden;background:var(--page);font-family:"Arimo",Arial,sans-serif}
.flyer{position:absolute;left:292px;top:62px;width:616px;height:875px;background:var(--pink);overflow:hidden;box-shadow:0 6px 18px rgba(0,0,0,.18)}
.flyer-bg{position:absolute;inset:0}
.brand{position:absolute;left:34px;top:30px;color:var(--white)}
.brand-name{display:flex;align-items:center;gap:8px;font-size:40px;font-weight:700;line-height:1;letter-spacing:-1px}
.brand-dot{width:26px;height:26px;border-radius:50%;background:var(--white)}
.brand-tag{font-size:11px;letter-spacing:.4px;margin:2px 0 0 42px}
.headline{position:absolute;left:32px;top:84px;color:var(--white);font-size:22px;font-weight:700;letter-spacing:-.3px}
.headline em{font-style:normal;color:var(--lime-pale)}
.subline{position:absolute;left:32px;top:114px;color:var(--white);font-size:13px}
.price-badge{position:absolute;left:398px;top:0;width:189px;height:124px;background:var(--lime-bright);border:3px solid var(--lime-pale);border-top:none;border-radius:0 0 10px 10px;text-align:center;color:var(--olive);box-shadow:0 3px 6px rgba(0,0,0,.15)}
.price-badge .from{font-size:15px;font-weight:700;margin-top:22px}
.price-badge .price{font-size:28px;font-weight:700;color:var(--pink);line-height:1.05}
.price-badge .note{font-size:12px;line-height:1.25;margin-top:2px}
.packages{position:absolute;left:32px;top:143px;width:553px;border-collapse:collapse;table-layout:fixed;font-size:13.5px;color:var(--ink)}
.packages td,.packages th{height:19.76px;border:1px solid var(--rule);padding:0 4px;font-weight:400;text-align:center;line-height:1}
.packages td:first-child{text-align:left}
.packages .price-row th{background:var(--pink);color:var(--white);border-color:#fff}
.packages tr:not(.price-row):not(.section) td{background:var(--white)}
.packages .section td{background:var(--lime);color:var(--pink);text-align:center !important}
.tick{color:var(--ink)}
.features{position:absolute;left:32px;top:655px;width:560px;display:flex;justify-content:space-between}
.feature{position:relative;width:108px;height:135px}
.feature svg.pin{position:absolute;inset:0}
.feature .shadow{position:absolute;left:24px;bottom:-8px;width:60px;height:8px;border-radius:50%;background:rgba(0,0,0,.25);filter:blur(3px)}
.feature .label{position:absolute;top:18px;left:0;width:100%;text-align:center;color:var(--pink);font-size:13.5px;line-height:1.2}
.feature .icon{position:absolute;left:34px;top:58px;width:40px;height:34px;border-radius:6px;background:var(--olive);opacity:.85}
.feature svg.icon-svg{position:absolute;left:34px;top:56px}
.footer{position:absolute;left:32px;top:812px;width:560px;display:flex;align-items:flex-start;color:var(--white)}
.footer .pitch{color:var(--lime-pale);font-weight:700;font-size:15.5px;line-height:1.45;width:220px}
.footer .divider{width:1px;height:44px;background:var(--white);margin:2px 16px 0 0}
.footer .cta{font-size:14px;line-height:1.45;width:182px}
.footer .contact{font-size:14px;line-height:1.3}
.footer .contact .phone{color:var(--lime-pale);font-weight:700;font-size:16px}
</style>
</head>
<body>
<div class="flyer">
  <svg class="flyer-bg" width="616" height="875" viewBox="0 0 616 875" aria-hidden="true">
    <defs>
      <linearGradient id="greenFade" x1="0" y1="0" x2="1" y2="1">
        <stop offset="0" stop-color="#8aa83a"/>
        <stop offset="1" stop-color="#b7d437"/>
      </linearGradient>
    </defs>
    <rect width="616" height="875" fill="#cc1687"/>
    <polygon points="0,340 616,420 616,560 0,470" fill="#e8147f"/>
    <polygon points="0,0 616,0 616,480 0,290" fill="url(#greenFade)"/>
    <polygon points="585,420 616,420 616,520 585,510" fill="#8e9a37"/>
  </svg>

  <div class="brand">
    <div class="brand-name"><span class="brand-dot"></span>corvex</div>
    <div class="brand-tag">YOUR LOCAL IT COMPANY</div>
  </div>
  <h1 class="headline">Affordable <em>IT Support</em> Packages</h1>
  <p class="subline">Peace of mind for your business at competitive prices</p>

  <div class="price-badge">
    <div class="from">IT Support from</div>
    <div class="price">£10pm</div>
    <div class="note">- from a trusted provider<br>based in Ashcombe</div>
  </div>

  <table class="packages">
    <colgroup><col style="width:218px"><col style="width:87px"><col style="width:86px"><col style="width:75px"><col style="width:87px"></colgroup>
    <tr class="price-row"><th>IT Support Packages</th><th>Remote</th><th>Plus</th><th>Pro</th><th>Unlimited</th></tr>
    <tr class="price-row"><th>Per Server</th><th>£45pm</th><th>£85pm</th><th>£85pm</th><th>£85pm</th></tr>
    <tr class="price-row"><th>Per Computers</th><th>£10pm</th><th>£10pm</th><th>£13pm</th><th>£15pm</th></tr>
    <tr class="section"><td colspan="5">Support service</td></tr>
    <tr><td>Server support</td><td>✓</td><td>✓</td><td>✓</td><td>✓</td></tr>
    <tr><td>PC/device support</td><td>✓</td><td>✓</td><td>✓</td><td>✓</td></tr>
    <tr class="section"><td colspan="5">Server/Network callout</td></tr>
    <tr><td>Remote support</td><td>✓</td><td>✓</td><td>✓</td><td>✓</td></tr>
    <tr><td>Onsite callout (4hr response)</td><td>£40</td><td>✓</td><td>✓</td><td>✓</td></tr>
    <tr><td>Hourly rate onsite</td><td>£25ph</td><td>Included</td><td>Included</td><td>Included</td></tr>
    <tr class="section"><td colspan="5">Computer/equipment/device callout</td></tr>
    <tr><td>Remote support</td><td>✓</td><td>✓</td><td>✓</td><td>✓</td></tr>
    <tr><td>Onsite callout (8hr response)</td><td>£40</td><td>£40</td><td>✓</td><td>✓</td></tr>
    <tr><td>Hourly rate onsite</td><td>£25ph</td><td>£25ph</td><td>Included</td><td>Included</td></tr>
    <tr class="section"><td colspan="5">Protection/Security</td></tr>
    <tr><td>Guardex anti-virus (per PC)</td><td>£2</td><td>£2</td><td>£2</td><td>✓</td></tr>
    <tr><td>Guardex content filter (per PC)</td><td>£1.30</td><td>£1.30</td><td>£1.30</td><td>✓</td></tr>
    <tr><td>Remote back-up (per unit, 5GB)</td><td>£1.50</td><td>£1.50</td><td>£1.50</td><td>✓</td></tr>
    <tr class="section"><td colspan="5">Monitoring</td></tr>
    <tr><td>Daily back-up checks</td><td>✓</td><td>✓</td><td>✓</td><td>✓</td></tr>
    <tr><td>24/7 monitoring</td><td>✓</td><td>✓</td><td>✓</td><td>✓</td></tr>
    <tr class="section"><td colspan="5">Maintenance</td></tr>
    <tr><td>Patch management</td><td>✓</td><td>✓</td><td>✓</td><td>✓</td></tr>
    <tr><td>Software updates</td><td>✓</td><td>✓</td><td>✓</td><td>✓</td></tr>
    <tr><td>Security updates</td><td>✓</td><td>✓</td><td>✓</td><td>✓</td></tr>
  </table>

  <div class="features">
    <div class="feature">
      <span class="shadow"></span>
      <svg class="pin" width="108" height="135" viewBox="0 0 108 135" aria-hidden="true"><path d="M54 132 C44 114 3 98 3 54 A51 51 0 1 1 105 54 C105 98 64 114 54 132Z" fill="#fff" stroke="#a9c93a" stroke-width="3"/></svg>
      <div class="label">Affordable,<br>local service</div>
      <div class="icon" role="img" aria-label="Computer with spanner and screwdriver icon"></div>
    </div>
    <div class="feature">
      <span class="shadow"></span>
      <svg class="pin" width="108" height="135" viewBox="0 0 108 135" aria-hidden="true"><path d="M54 132 C44 114 3 98 3 54 A51 51 0 1 1 105 54 C105 98 64 114 54 132Z" fill="#fff" stroke="#a9c93a" stroke-width="3"/></svg>
      <div class="label">4 hour<br>callout</div>
      <svg class="icon-svg" width="40" height="40" viewBox="0 0 40 40" aria-label="Phone icon" role="img">
        <circle cx="20" cy="20" r="17" fill="none" stroke="#7d8f2a" stroke-width="3"/>
        <path d="M16 9 h5 v6 h-3 c0 4 0 6 0 10 h3 v6 h-5 c-3-3-4-7-4-11 s1-8 4-11z" fill="#7d8f2a"/>
      </svg>
    </div>
    <div class="feature">
      <span class="shadow"></span>
      <svg class="pin" width="108" height="135" viewBox="0 0 108 135" aria-hidden="true"><path d="M54 132 C44 114 3 98 3 54 A51 51 0 1 1 105 54 C105 98 64 114 54 132Z" fill="#fff" stroke="#a9c93a" stroke-width="3"/></svg>
      <div class="label">Remote<br>support</div>
      <div class="icon" role="img" aria-label="Two connected computers icon"></div>
    </div>
    <div class="feature">
      <span class="shadow"></span>
      <svg class="pin" width="108" height="135" viewBox="0 0 108 135" aria-hidden="true"><path d="M54 132 C44 114 3 98 3 54 A51 51 0 1 1 105 54 C105 98 64 114 54 132Z" fill="#fff" stroke="#a9c93a" stroke-width="3"/></svg>
      <div class="label">24/7<br>monitoring</div>
      <div class="icon" role="img" aria-label="24/7 clock icon" style="border-radius:50%"></div>
    </div>
    <div class="feature">
      <span class="shadow"></span>
      <svg class="pin" width="108" height="135" viewBox="0 0 108 135" aria-hidden="true"><path d="M54 132 C44 114 3 98 3 54 A51 51 0 1 1 105 54 C105 98 64 114 54 132Z" fill="#fff" stroke="#a9c93a" stroke-width="3"/></svg>
      <div class="label">Server/PC<br>builds from<br>£250</div>
      <div class="icon" role="img" aria-label="Server tower icon" style="left:42px;width:24px;top:70px;height:34px"></div>
    </div>
  </div>

  <div class="footer">
    <p class="pitch">Protect your business and keep downtime costs at bay</p>
    <span class="divider"></span>
    <p class="cta">Call, email or live chat with us on our website today!</p>
    <span class="divider"></span>
    <div class="contact">
      <div class="phone">01632 960 418</div>
      <div>info@corvex.co.uk</div>
      <div>www.corvex.co.uk</div>
    </div>
  </div>
</div>
</body>
</html>
```